Lyrebell Wedding Bombonieries

Wedding Bomboniere

these are for wedding favors I have a logo and a pic that I would like to add not sure how to send through to you also card shouls be a wedding theme

Target Market(s)

brides

Industry/Entity Type

Wedding

Contact Information for Business Card

Marguerite Oslowski
0432 591 604
email dorvin@plumtelnet.com.au
www.lyrebell.com.au

```html
<!DOCTYPE html>
<html lang="en">
<head>
<meta charset="utf-8">
<title>Lyrebell Wedding Bombonieries – Business Card</title>
<link href="https://fonts.googleapis.com/css2?family=Great+Vibes&family=Marcellus&display=swap" rel="stylesheet">
<style>
  :root {
    --page: #ffffff;
    --gold-deep: #c17d17;
    --gold-mid: #d9a862;
    --gold-light: #f3e6c8;
    --blue: #1a8ee8;
    --ink: #1b1b1b;
    --tray-light: #e9f1f4;
    --tray-blue: #2bc0f5;
    --tray-deep: #1a6de0;
    --frame-gold: #f2b54a;
  }
  * { margin: 0; padding: 0; box-sizing: border-box; }
  html, body { width: 1200px; height: 979px; overflow: hidden; background: var(--page); }
  .canvas { position: relative; width: 1200px; height: 979px; }

  .card {
    position: absolute; left: 0; top: 0; width: 1147px; height: 735px;
    border-radius: 34px;
    background: linear-gradient(100deg, var(--gold-deep) 0%, var(--gold-light) 30%, var(--gold-mid) 55%, var(--gold-light) 100%);
  }
  .card-face {
    position: absolute; left: 27px; top: 27px; width: 1093px; height: 682px;
    border-radius: 14px;
    background:
      radial-gradient(ellipse 380px 240px at 150px 120px, rgba(255,245,220,.55), transparent 70%),
      linear-gradient(160deg, #c98a25 0%, #e0b775 30%, #c17d17 55%, #dcae68 80%, #e6c07f 100%);
  }

  .owner-name {
    position: absolute; left: 150px; top: 135px; width: 450px; text-align: center;
    font-family: "Great Vibes", cursive; font-size: 60px; line-height: 70px; color: var(--blue); white-space: nowrap;
  }
  .owner-phone {
    position: absolute; left: 150px; top: 207px; width: 450px; text-align: center;
    font-family: "Marcellus", serif; font-size: 27px; line-height: 34px; color: var(--ink); letter-spacing: 1px;
  }
  .contact {
    position: absolute; left: 640px; top: 132px; width: 370px; text-align: center;
    font-family: "Marcellus", serif; font-size: 25px; line-height: 39px; color: var(--ink); letter-spacing: .5px;
  }

  .brand { position: absolute; left: 130px; top: 300px; width: 420px; text-align: center; }
  .brand-name {
    font-family: "Great Vibes", cursive; font-size: 82px; line-height: 100px; color: var(--ink);
  }
  .brand-line {
    font-family: "Marcellus", serif; font-size: 54px; line-height: 64px; color: var(--blue);
  }

  .product-art { position: absolute; left: 505px; top: 257px; width: 524px; height: 418px; }
</style>
</head>
<body>
<div class="canvas">
  <div class="card">
    <div class="card-face"></div>

    <div class="owner-name">Marguerite Oslowski</div>
    <div class="owner-phone">0432 591 604</div>

    <div class="contact">
      <div>dorvin@plumtelnet.com.au</div>
      <div>www.lyrebell.com.au</div>
    </div>

    <div class="brand">
      <div class="brand-name">Lyrebell</div>
      <div class="brand-line">Wedding</div>
      <div class="brand-line">Bombonieries</div>
    </div>

    <svg class="product-art" viewBox="0 0 524 418" xmlns="http://www.w3.org/2000/svg">
      <defs>
        <linearGradient id="favourFill" x1="0" y1="0" x2="1" y2="1">
          <stop offset="0" stop-color="var(--tray-light)"/>
          <stop offset="0.55" stop-color="var(--tray-blue)"/>
          <stop offset="1" stop-color="var(--tray-deep)"/>
        </linearGradient>
      </defs>
      <g class="gold-frames" fill="none" stroke="var(--frame-gold)" stroke-width="3" opacity=".9">
        <rect x="100" y="45" width="360" height="370" transform="rotate(4 280 230)"/>
        <rect x="90" y="55" width="380" height="350" transform="rotate(-3 280 230)"/>
        <rect x="110" y="40" width="350" height="380" transform="rotate(8 280 230)"/>
      </g>
      <rect class="favour-illustration" x="4" y="40" width="519" height="314" rx="40"
            fill="url(#favourFill)" opacity=".9" role="img"
            aria-label="Illustration of groom and bride favour boxes beside a ring box of heart chocolates on a blue tray"/>
    </svg>
  </div>
</div>
</body>
</html>
```